Custom Sales & Marketing Trifold

Need to develop a tri-fold marketing flyer that can have images easily customized and sent to specific clients electronically or via mail on an ad-hoc basis.

2 examples of flyers we created internally are attached for example of the general message we're trying to send to the client. Also have attached some images to use as examples as well as company logo files you are free to use.
Updates

Most designers did not follow directions for this brief, and those that did we did not like the design, and as such we will not be making an award for this project. Thank you, Derek

Industry/Entity Type

Marketing

Requirements
Must have
• Must have placeholders for images where we can change images for custom use. In addition, must include our contact information as well as the fact facts information. Feel free to edit wording as you see fit.

```html
<!DOCTYPE html>
<html lang="en">
<head>
<meta charset="utf-8">
<title>Northwind Aviation Solutions – Trifold</title>
<link rel="stylesheet" href="https://fonts.googleapis.com/css2?family=Arimo:wght@400;700&family=Archivo+Black&display=swap">
<style>
  :root{
    --cyan:#2cc6e6;
    --teal:#17687f;
    --teal-dark:#0f4f62;
    --yellow:#f9b914;
    --red:#d3213c;
    --white:#ffffff;
    --ink:#111111;
    --stage:#e3e3e3;
    --sky:#9fb9cf;
    --tarmac:#8a8f94;
    --cabin-warm:#b99a7e;
    --cabin-light:#d9d3c8;
  }
  *{box-sizing:border-box;margin:0;padding:0}
  html,body{width:1200px;height:900px;overflow:hidden;background:var(--stage);font-family:"Arimo",Arial,sans-serif}
  .sheet{position:absolute;left:60px;top:90px;width:1080px;height:720px;display:flex;box-shadow:0 10px 30px rgba(0,0,0,.18)}
  .panel{position:relative;width:360px;height:720px;overflow:hidden}

  /* Cover panel */
  .cover{background:var(--white)}
  .cover-photo{position:absolute;left:0;top:0;width:360px;height:250px;background:linear-gradient(180deg,var(--sky) 0%,#dfe6ec 55%,var(--tarmac) 100%)}
  .cover-stripe{position:absolute;left:0;top:0}
  .brand-card{position:absolute;right:0;top:200px;width:240px;height:90px;background:var(--white);display:flex;align-items:center;justify-content:center;padding:0 10px}
  .brand-name{font-family:"Arimo",Arial,sans-serif;font-weight:400;color:var(--teal-dark);font-size:15px;white-space:nowrap}
  .compass-art{position:absolute;left:38px;top:318px;width:110px;height:110px;border-radius:50%;background:radial-gradient(circle,#c7d3e0 0%,#6f859c 70%,rgba(111,133,156,0) 72%)}
  .cover-tagline{position:absolute;left:0;top:0}
  .tag-word{font-family:"Archivo Black","Arimo",sans-serif;fill:var(--ink)}

  /* Middle panel */
  .middle{background:var(--teal)}
  .paper-intro{position:absolute;left:0;top:0;width:360px;height:200px;background:var(--cyan);padding:22px 26px 0 34px}
  .paper-intro .glow{position:absolute;left:150px;top:70px;width:90px;height:90px;border-radius:50%;background:var(--yellow)}
  .paper-intro h2{position:relative;font-size:19px;font-weight:700;color:var(--ink);margin-bottom:8px}
  .paper-intro p{position:relative;font-size:12.5px;line-height:1.35;color:var(--ink)}
  .data-card{position:absolute;left:30px;width:310px;background:var(--white);padding:8px 10px}
  .data-card.costs{top:220px}
  .data-card.fleet{top:400px}
  .data-card h3{font-size:11px;color:var(--teal-dark);margin-bottom:4px}
  .data-card table{width:100%;border-collapse:collapse;font-size:10px}
  .data-card th{background:var(--teal);color:var(--white);text-align:left;padding:3px 4px}
  .data-card td{padding:3px 4px;border-bottom:1px solid #d5dde2;color:#333}
  .data-card tr:nth-child(even) td{background:#eef5f8}
  .contact-block{position:absolute;left:0;bottom:0;width:360px;height:160px;background:var(--yellow);padding:12px 30px 0 70px;color:var(--white);font-size:12px;line-height:1.38;font-style:normal}
  .contact-block .company{font-weight:700}
  .contact-block .mark{position:absolute;left:0;top:0}

  /* Inside-right panel */
  .gallery{background:var(--teal)}
  .benefits{position:absolute;left:0;top:0;width:360px;height:180px;background:var(--cyan);padding:22px 22px 0 30px}
  .benefits .glow{position:absolute;left:-30px;top:60px;width:110px;height:110px;border-radius:50%;background:var(--yellow)}
  .benefits ul{position:relative;list-style:none;font-size:12.5px;line-height:1.35;color:var(--ink)}
  .benefits li{margin-bottom:6px;padding-left:12px;position:relative}
  .benefits li::before{content:"";position:absolute;left:0;top:6px;width:5px;height:5px;border-radius:50%;background:var(--ink)}
  .photo-slot{position:absolute;left:40px;width:320px}
  .photo-slot.cabin-one{top:180px;height:205px;background:linear-gradient(160deg,var(--cabin-light) 0%,var(--cabin-warm) 60%,#7a5a45 100%)}
  .photo-slot.cabin-two{top:415px;height:215px;background:linear-gradient(200deg,#eef0ee 0%,var(--cabin-light) 45%,#9c8f80 100%)}
  .yellow-bar{position:absolute;left:40px;width:320px;height:14px;background:var(--yellow)}
  .yellow-bar.top{top:392px}
  .yellow-bar.bottom{top:636px}
  .gallery .frame{position:absolute;left:0;top:180px;width:40px;height:540px;background:var(--cyan)}
</style>
</head>
<body>
<main class="sheet">

  <section class="panel cover">
    <div class="cover-photo" role="img" aria-label="Photo of a private jet parked on the tarmac"></div>
    <svg class="cover-stripe" width="360" height="720" viewBox="0 0 360 720">
      <polygon points="0,0 40,0 40,120 0,150" fill="var(--cyan)"/>
      <polygon points="0,250 180,215 220,250 0,300" fill="var(--cyan)"/>
      <polygon points="60,250 150,230 190,260 80,275" fill="var(--red)"/>
      <rect x="0" y="300" width="360" height="420" fill="var(--white)"/>
    </svg>
    <div class="brand-card">
      <span class="brand-name">Northwind Aviation Solutions</span>
    </div>
    <div class="compass-art" role="img" aria-label="Compass rose decoration"></div>
    <svg class="cover-tagline" width="360" height="720" viewBox="0 0 360 720">
      <rect x="18" y="352" width="16" height="12" fill="var(--teal)"/>
      <rect x="170" y="372" width="12" height="16" fill="var(--teal)"/>
      <rect x="60" y="445" width="14" height="10" fill="var(--teal)"/>
      <rect x="20" y="490" width="10" height="14" fill="var(--teal)"/>
      <rect x="200" y="430" width="10" height="10" fill="var(--teal)"/>
      <polygon points="130,480 360,470 360,720 90,720 110,600" fill="var(--teal)"/>
      <polygon points="90,700 360,690 360,720 90,720" fill="var(--yellow)"/>
      <rect x="0" y="680" width="36" height="40" fill="var(--teal)"/>
      <text class="tag-word" x="145" y="525" font-size="34">DRIVE</text>
      <g fill="var(--white)" stroke="var(--ink)" stroke-width="2">
        <polygon points="267,545 289,545 289,568 303,568 278,598 253,568 267,568"/>
      </g>
      <text class="tag-word" x="150" y="615" font-size="30">Cost</text>
      <text class="tag-word" x="150" y="672" font-size="30">Service</text>
    </svg>
  </section>

  <section class="panel middle">
    <div class="paper-intro">
      <span class="glow"></span>
      <h2>Don't Forget the Paperwork!</h2>
      <p>Every flight leaves a trail of records. Our team tracks logbooks, invoices and compliance files so your owners see clear monthly reports, lower costs and no surprises at audit time. We handle the details while you enjoy the flight.</p>
    </div>
    <div class="data-card costs">
      <h3>Monthly Cost Summary</h3>
      <table>
        <tr><th>Item</th><th>Budget</th><th>Actual</th></tr>
        <tr><td>Fuel</td><td>42,100</td><td>40,860</td></tr>
        <tr><td>Crew</td><td>28,500</td><td>28,500</td></tr>
        <tr><td>Hangar</td><td>9,200</td><td>8,940</td></tr>
        <tr><td>Maintenance</td><td>15,300</td><td>14,120</td></tr>
      </table>
    </div>
    <div class="data-card fleet">
      <h3>Fleet Utilization</h3>
      <table>
        <tr><th>Month</th><th>Hours</th><th>Trips</th><th>Rate</th></tr>
        <tr><td>Jan</td><td>62</td><td>18</td><td>94%</td></tr>
        <tr><td>Feb</td><td>58</td><td>16</td><td>91%</td></tr>
        <tr><td>Mar</td><td>71</td><td>21</td><td>96%</td></tr>
      </table>
    </div>
    <address class="contact-block">
      <svg class="mark" width="60" height="160" viewBox="0 0 60 160"><polygon points="0,0 60,0 0,115" fill="var(--teal)"/></svg>
      <div class="company">Northwind Aviation Solutions</div>
      <div>Derek, Client Services</div>
      <div>1420 Hangar Way, Suite 3</div>
      <div>Ridgefield, CA 90210</div>
      <div>(555) 014-2090</div>
      <div>derek@northwindair.example</div>
      <div>www.northwindair.example</div>
    </address>
  </section>

  <section class="panel gallery">
    <div class="benefits">
      <span class="glow"></span>
      <ul>
        <li>Each aircraft receives a dedicated manager who answers owner questions within one business day.</li>
        <li>Transparent pricing with detailed statements and cost benchmarks against similar aircraft types.</li>
        <li>Owner trips planned, staffed and reviewed so every flight is handled thoroughly.</li>
      </ul>
    </div>
    <div class="frame"></div>
    <div class="photo-slot cabin-one" role="img" aria-label="Photo of a private jet cabin with leather seating"></div>
    <div class="yellow-bar top"></div>
    <div class="photo-slot cabin-two" role="img" aria-label="Photo of a bright jet cabin lounge area"></div>
    <div class="yellow-bar bottom"></div>
  </section>

</main>
</body>
</html>
```